Multi Disciplinary Health Clinic Needs a Pop Up Banner

Brightway Health needs a pop up banner ( approx. 33" x 80") to use at marketing events. We offer Chiropractic, Massage Therapy, Acupuncture, Laser Therapy, Shockwave Therapy and a lot of other modalities. We have a diverse client base ranging from children to professional athletes. More info about our clinic can be found at www.brightwayhealth.ca

Target Market(s)

potential patients, all age ranges, people who are in pain or are wanting to improve their health

Industry/Entity Type

Health And Wellness

Font styles to use
Sans Serif

Requirements
Must have
• our logo
• serives: chiropractic, massage therapy, shockwave, laser
• our logo colours as the basis for the colour theme
• our website address
Nice to have
• our phone number
• images from our website ( i have high resolution files of all images)
• word font that fits with our logo font
Should not have
• an abundance of spa massage pictures. we focus more on the rehabilitation of pain and injury.

```html
<!DOCTYPE html>
<html lang="en">
<head>
<meta charset="utf-8">
<title>Brightway Health – Pop Up Banner</title>
<link href="https://fonts.googleapis.com/css2?family=Arimo:wght@400;700&display=swap" rel="stylesheet">
<style>
:root{
  --blue:#1b67b0;
  --blue-dark:#15558f;
  --orange:#f47b20;
  --grey:#6b6c6e;
  --white:#ffffff;
}
*{margin:0;padding:0;box-sizing:border-box}
html,body{width:1200px;height:2909px;overflow:hidden;background:var(--white)}
body{font-family:"Arimo",Arial,sans-serif}
.banner{position:relative;width:1200px;height:2909px;overflow:hidden;background:var(--white)}

.brand{position:absolute;left:80px;top:120px;display:flex;align-items:center;gap:30px}
.brand-dot{width:150px;height:150px;border-radius:50%;background:var(--blue)}
.brand-name{font-weight:700;font-size:88px;color:var(--blue);letter-spacing:1px}

.headline{position:absolute;left:94px;top:385px;font-weight:700;line-height:1;letter-spacing:-1px}
.headline .line{display:block;color:var(--blue);font-size:128px;margin-bottom:14px}
.headline .accent{display:block;color:var(--orange);font-size:158px;margin-top:18px}

.family-photo{position:absolute;left:0;top:836px;width:1200px;height:900px;
  background:radial-gradient(ellipse at 35% 40%,#e9d3c2 0%,#c9b59c 25%,transparent 55%),
             linear-gradient(180deg,#f4f1e8 0%,#cfd6a8 35%,#7fa64a 70%,#5f8e2f 100%)}

.band-top{position:absolute;left:0;top:1690px;width:1200px;height:80px}
.services-band{position:absolute;left:0;top:1740px;width:1200px;height:690px;background:var(--blue)}

.tag{position:absolute;background:var(--orange);color:var(--white);font-weight:700;
  font-size:46px;letter-spacing:1px;display:flex;align-items:center;padding-left:30px;
  clip-path:polygon(0 0,100% 0,93% 50%,100% 100%,0 100%)}
.tag-services{left:97px;top:1862px;width:470px;height:72px}
.tag-book{left:108px;top:2452px;width:462px;height:72px}

.service-list{position:absolute;left:92px;top:1970px;list-style:none}
.service-list li{color:var(--white);font-weight:700;font-size:58px;height:79px;display:flex;align-items:center}
.service-list li::before{content:"";width:24px;height:24px;border-radius:50%;background:#f6a21e;margin-right:30px;flex:none}
.service-list .more{color:var(--orange);margin-left:16px}

.treatment{position:absolute;width:470px;height:470px;border-radius:50%;border:12px solid var(--white);
  box-shadow:0 6px 18px rgba(0,0,0,.3)}
.treatment-neck{left:675px;top:1282px;background:radial-gradient(circle at 60% 40%,#c89377 0%,#a67159 45%,#5a4a44 100%)}
.treatment-back{left:675px;top:1645px;background:radial-gradient(circle at 45% 60%,#d7a98c 0%,#b7876b 40%,#3e3b3d 100%)}
.treatment-laser{left:675px;top:2008px;background:radial-gradient(circle at 40% 55%,#e9c3b0 0%,#d9a891 40%,#eef0f3 100%)}

.website{position:absolute;left:100px;top:2568px;font-weight:700;font-size:66px;color:var(--blue)}

.footer{position:absolute;left:0;top:2686px;width:1200px;height:223px;background:var(--grey)}
.footer .phone{position:absolute;left:97px;top:38px;color:var(--white);font-weight:700;font-size:48px}
.footer .email{position:absolute;left:97px;top:108px;color:var(--white);font-size:38px}
.social{position:absolute;top:53px;width:98px;height:98px;border-radius:50%;background:var(--orange)}
.social-one{left:892px}
.social-two{left:1020px}
</style>
</head>
<body>
<main class="banner">
  <header class="brand">
    <span class="brand-dot"></span>
    <span class="brand-name">Brightway Health</span>
  </header>

  <h1 class="headline">
    <span class="line">Helping You</span>
    <span class="line">Live Life</span>
    <span class="accent">PAIN FREE</span>
  </h1>

  <div class="family-photo" role="img" aria-label="Happy family of four playing together on the grass in a sunny park"></div>

  <svg class="band-top" viewBox="0 0 1200 80" preserveAspectRatio="none" aria-hidden="true">
    <path d="M0 30 Q600 -10 1200 40 L1200 80 L0 80 Z" fill="var(--orange)"/>
    <path d="M0 50 Q600 10 1200 60 L1200 80 L0 80 Z" fill="var(--blue)"/>
  </svg>

  <section class="services-band">
  </section>

  <div class="tag tag-services">OUR SERVICES</div>
  <ul class="service-list">
    <li>Chiropractic</li>
    <li>Massage</li>
    <li>Acupuncture</li>
    <li>Shockwave</li>
    <li>Laser<span class="more">and more</span></li>
  </ul>

  <div class="treatment treatment-neck" role="img" aria-label="Shockwave applicator treating a patient's neck"></div>
  <div class="treatment treatment-back" role="img" aria-label="Therapist massaging a patient's back"></div>
  <div class="treatment treatment-laser" role="img" aria-label="Laser therapy device on a patient's shoulder"></div>

  <div class="tag tag-book">BOOK NOW!!</div>
  <p class="website">www.brightwayhealth.ca</p>

  <footer class="footer">
    <p class="phone">Call : (403) 555-0148</p>
    <p class="email">Email: info@brightwayhealth.ca</p>
    <span class="social social-one"></span>
    <span class="social social-two"></span>
  </footer>
</main>
</body>
</html>
```